Responsive Wordpress Site Design - Veterans Job Site

I need a re-design of my web page, www.brivoltcareers.com. I want it to be Responsive so it looks great on mobile. I am a job recruiter for military veterans in the U.S. Here is a sample re-design site that a different developer just finished for me: http://brivoltcareers.com/test/ I fired him because I got frustrated with his design abilities. But, this site is the general idea of what I want. I want the colors to be red, white and blue. I like a lot of white space so, big type, and video/pictures so it's easy on the eyes. I like this page: http://plumforkswing.com/ . I do a lot with videos (that's how I present my veterans to companies, testimonials, job tips) so I would like to have a lot of video on the page. I want the home page to be one long scrolling page so it is easy to navigate on mobile and I can load it with keywords for SEO. I want the page to have a patriotic and powerful feel.

Target Market(s)

I have two audiences: Veterans looking for jobs and Companies looking to hire jobs. Right now I focus on the state of Connecticut, but next month I'm expanding to Massachusetts and I have plans to expand nationwide.

Industry/Entity Type

Marketing

Font styles to use
Sans Serif

Colors
ec1f27
0455a3
ffffff

Requirements
Must have
• Lots of ClipTube videos...overviews of how the company works (I'll create this videos later, just use a placeholder for now), testimonials, job tips
• Social media feeds for Facenote and Chirper
• Big pictures
• Top section big and clear for Veterans to "Register Free"...this will bounce to my registration page...the most important goal of the site.
• Big and clear way for Companies to complete a form to request more information.
• Highlight videos of testimonials...the success stories
• Big headlines and text so the page is easy on the eyes and easy to read on a mobile phone.
• Lots of white space
• A professional look...want viewers to see the company as a strong
• I need the ability to edit the page when you're done....to add forms, additional pages, etc.
Nice to have
• see must haves
Should not have
• see must haves

```html
<!DOCTYPE html>
<html lang="en">
<head>
<meta charset="utf-8">
<title>Brivolt Careers – Job Placement for Military Veterans</title>
<link rel="stylesheet" href="https://fonts.googleapis.com/css2?family=Raleway:wght@600;700;800&family=Open+Sans:ital,wght@0,400;0,600;0,700;1,400&display=swap">
<style>
:root{
  --red:#d8343c;
  --red-dark:#b8262d;
  --blue:#2b4c96;
  --blue-dark:#1f3a7a;
  --navy:#22407f;
  --cyan:#2bc0d6;
  --text:#4a4a4a;
  --muted:#777;
  --line:#dcdcdc;
  --grey-bg:#efefef;
  --white:#ffffff;
}
*{box-sizing:border-box;margin:0;padding:0}
html,body{width:1200px;height:3232px;overflow:hidden}
body{position:relative;background:var(--white);font-family:"Open Sans",Arial,sans-serif;color:var(--text)}
.abs{position:absolute}
h1,h2,h3,h4{font-family:"Raleway",Arial,sans-serif}
.btn{position:absolute;display:flex;align-items:center;justify-content:center;color:#fff;font-family:"Raleway",Arial,sans-serif;font-weight:700;font-size:14px;text-transform:uppercase;border-radius:3px;text-decoration:none}
.btn-red{background:var(--red);box-shadow:inset 0 -3px 0 var(--red-dark)}
.btn-blue{background:var(--blue);box-shadow:inset 0 -3px 0 var(--blue-dark)}

/* header */
.site-header{position:absolute;left:0;top:0;width:1200px;height:143px;background:#fff}
.phone{position:absolute;left:97px;top:46px;display:flex;align-items:center;gap:14px;font-family:"Raleway",Arial,sans-serif;font-weight:700;font-size:16px;color:var(--blue)}
.phone-icon{width:44px;height:44px;border:2px solid var(--blue);border-radius:50%;display:flex;align-items:center;justify-content:center}
.brand{position:absolute;left:480px;top:42px;width:240px;display:flex;align-items:center;gap:10px;font-family:"Raleway",Arial,sans-serif;font-weight:800;font-size:26px;color:var(--blue);text-transform:uppercase}
.brand-dot{width:40px;height:40px;border-radius:50%;background:var(--red)}
.register-top{left:938px;top:43px;width:162px;height:49px}

/* nav */
.main-nav{position:absolute;left:0;top:143px;width:1200px;height:49px;background:linear-gradient(#3a5ba6,#2a4a92)}
.main-nav ul{list-style:none;display:flex;height:49px;margin-left:99px}
.main-nav li{height:49px;padding:0 24px;display:flex;align-items:center;color:#fff;font-size:13px;text-transform:uppercase}
.main-nav li.active{background:var(--red);padding:0 40px}

/* hero */
.hero{position:absolute;left:0;top:192px;width:1200px;height:556px;background:linear-gradient(180deg,#3f4a52 0%,#6b6f6a 45%,#a59a86 75%,#5a5650 100%)}
.hero-title{position:absolute;left:0;top:138px;width:1200px;text-align:center;font-family:"Raleway",Arial,sans-serif;font-weight:800;font-size:50px;color:#fff;letter-spacing:1px;text-shadow:0 2px 6px rgba(0,0,0,.4)}
.hero-title .hl{color:var(--red)}
.hero-title .hb{color:#4a78d0}
.hero-sub{position:absolute;left:0;top:210px;width:1200px;text-align:center;font-family:"Raleway",Arial,sans-serif;font-weight:700;font-size:17px;line-height:30px;color:#fff;text-transform:uppercase}
.hero-people{position:absolute;left:70px;top:280px;width:560px;height:276px;background:linear-gradient(90deg,#3a3a3e,#6a5848 35%,#4b5561 70%,#7a7e6a);opacity:.85}
.hero-arrow{position:absolute;top:250px}
.hero-dot{position:absolute;left:503px;top:532px;width:12px;height:12px;border-radius:50%;background:#222}

/* intro */
.section-title{font-family:"Raleway",Arial,sans-serif;font-weight:700;font-size:34px;text-transform:uppercase;color:var(--blue);letter-spacing:.5px}
.section-title .r{color:var(--red)}
.intro-title{left:97px;top:806px}
.intro-sub{left:97px;top:862px;font-family:"Raleway",Arial,sans-serif;font-weight:700;font-size:15px;color:#333;text-transform:uppercase}
.intro-divider{left:561px;top:812px;width:1px;height:178px;background:var(--line)}
.intro-text{left:605px;top:808px;width:495px;font-size:14px;line-height:26px;color:var(--text)}
.intro-rule{left:97px;top:992px;width:1004px;height:1px;background:var(--line)}

.card{position:absolute;top:1044px;width:297px;height:273px;border:1px solid var(--line);text-align:center;background:#fff}
.card svg{margin-top:32px}
.card h3{margin-top:26px;font-size:15px;font-weight:700;color:#333;text-transform:uppercase}
.card p{margin:14px auto 0;width:250px;font-size:13px;line-height:24px;color:var(--text)}

/* videos */
.videos{position:absolute;left:0;top:1380px;width:1200px;height:625px;background:var(--grey-bg)}
.videos-title{left:97px;top:35px}
.videos-lead{left:97px;top:80px;width:1004px;font-size:13.5px;line-height:26px}
.player{position:absolute;left:97px;top:165px;width:528px;height:310px;background:#222}
.player-bar-top{position:absolute;left:0;top:0;width:528px;height:34px;background:rgba(40,40,40,.9);color:#ddd;font-size:14px;line-height:34px;padding-left:18px}
.player-photo{position:absolute;left:0;top:34px;width:528px;height:240px;background:linear-gradient(135deg,#b9c6d3,#8e9aa8 50%,#c9d0d6)}
.play-btn{position:absolute;width:74px;height:74px;border-radius:50%;background:rgba(20,20,20,.75);display:flex;align-items:center;justify-content:center}
.player-bar{position:absolute;left:0;bottom:0;width:100%;height:36px;background:#1b1b1b;color:#ccc;font-size:12px;display:flex;align-items:center;padding:0 16px;gap:18px}
.player-bar .brandname{margin-left:auto;font-weight:700;color:#fff;font-size:14px}
.progress{position:absolute;left:0;bottom:36px;width:100%;height:4px;background:#555}
.progress::before{content:"";position:absolute;left:0;top:0;width:14px;height:4px;background:var(--red)}
.overview-h{left:97px;top:505px;font-family:"Raleway",Arial,sans-serif;font-weight:700;font-size:15px;color:var(--blue);text-transform:uppercase}
.overview-p{left:97px;top:530px;width:528px;font-size:13.5px;line-height:26px}
.more{color:var(--red);text-transform:uppercase}
.thumb{position:absolute;left:690px;width:183px;height:107px;background:linear-gradient(135deg,#6f7a86,#a59c8c)}
.thumb .play-btn{width:34px;height:34px;left:74px;top:36px;background:#fff}
.thumb-text{position:absolute;left:904px;width:200px;font-size:13px;line-height:25px}

/* social */
.social-title{left:97px;top:2055px}
.panel{position:absolute;top:2120px;width:473px;height:333px;background:#f2f2f2}
.panel-head{height:40px;display:flex;align-items:center;padding:0 14px;color:#fff;font-family:"Raleway",Arial,sans-serif;font-weight:700;font-size:18px}
.panel-fb{left:97px}
.panel-fb .panel-head{background:var(--navy)}
.panel-tw{left:628px}
.panel-tw .panel-head{background:var(--cyan)}
.feed{position:absolute;left:0;width:473px;height:95px;border-bottom:1px solid #e0e0e0}
.feed .avatar{position:absolute;left:0;top:18px;width:62px;height:62px}
.feed .bird{position:absolute;left:22px;top:20px;width:20px;height:20px;border-radius:50%;background:var(--cyan)}
.feed p{position:absolute;left:78px;top:12px;width:380px;font-size:13px;line-height:24px;color:var(--text)}
.feed small{position:absolute;left:78px;top:64px;font-size:10.5px;color:var(--blue)}
.panel-tw .feed small{color:var(--cyan)}

/* testimonials */
.testimonials{position:absolute;left:0;top:2510px;width:1200px;height:360px;background:linear-gradient(90deg,#dfe6ee,#c8d4e0 50%,#dbe3eb)}
.testi-title{left:97px;top:35px}
.testi-video{position:absolute;left:97px;top:110px;width:398px;height:208px;background:#222}
.testi-photo{position:absolute;left:0;top:0;width:398px;height:168px;background:linear-gradient(135deg,#4a4c3a,#8a7a55 50%,#2e2e28)}
.quote{position:absolute;left:560px;top:112px;width:540px;font-style:italic;font-size:14.5px;line-height:26px;color:#555;text-indent:40px}
.qmark{position:absolute;font-family:Georgia,serif;font-size:60px;color:#999;line-height:1}
.testi-name{position:absolute;right:100px;top:300px;font-size:13px;color:var(--red);text-transform:uppercase}
.testi-name span{color:#666;text-transform:none;font-size:11px}
.circle-arrow{position:absolute;top:2710px;width:34px;height:34px;border-radius:50%;background:#9a9a9a;display:flex;align-items:center;justify-content:center}

/* footer */
.footer-h{position:absolute;top:2918px;font-family:"Raleway",Arial,sans-serif;font-weight:700;font-size:15px;color:var(--blue);text-transform:uppercase}
.links{position:absolute;top:2970px;list-style:none;font-size:13px;line-height:26px;color:#444}
.links li::before{content:"›";margin-right:14px;color:#444}
.loop-text{position:absolute;left:460px;top:2965px;width:450px;font-size:13px;line-height:26px}
.field{position:absolute;left:460px;width:300px;height:34px;border:1px solid #bbb;font-size:13px;padding-left:8px;line-height:32px;color:#555}
.subscribe{left:460px;top:3113px;width:103px;height:33px;font-family:"Open Sans",Arial,sans-serif;font-weight:400;text-transform:none;font-size:13px}
.follow{position:absolute;left:990px;display:flex;align-items:center;gap:14px;font-size:13px;color:#444}
.follow i{width:28px;height:28px;border-radius:50%;display:block}
.bottom-bar{position:absolute;left:0;top:3178px;width:1200px;height:54px;background:var(--navy);color:#fff;font-size:12px;font-weight:700;display:flex;align-items:center;padding-left:97px;text-transform:uppercase}
.bottom-bar .up{position:absolute;left:1070px;top:12px;width:30px;height:30px;border-radius:50%;border:1px solid rgba(255,255,255,.5)}
</style>
</head>
<body>

<header class="site-header">
  <div class="phone">
    <span class="phone-icon"><svg width="20" height="20" viewBox="0 0 24 24"><path d="M6.6 10.8c1.4 2.8 3.8 5.1 6.6 6.6l2.2-2.2c.3-.3.7-.4 1-.2 1.1.4 2.3.6 3.6.6.6 0 1 .4 1 1V20c0 .6-.4 1-1 1C10.6 21 3 13.4 3 4c0-.6.4-1 1-1h3.5c.6 0 1 .4 1 1 0 1.3.2 2.5.6 3.6.1.3 0 .7-.2 1L6.6 10.8z" fill="#2b4c96"/></svg></span>
    CALL US: (203) 555-0147
  </div>
  <div class="brand"><span class="brand-dot"></span>Brivolt Careers</div>
  <a class="btn btn-red register-top">&#9679;&nbsp; Register Free</a>
</header>

<nav class="main-nav">
  <ul>
    <li class="active">Home</li><li>About Us</li><li>Job Openings</li><li>Apply Now</li><li>Interested Employers</li><li>Testimonials</li><li>Blog</li><li>Contact Us</li>
  </ul>
</nav>

<section class="hero" role="img" aria-label="Photo of helicopters at dusk with three smiling veterans in work uniforms">
  <h1 class="hero-title">WE RECRUIT <span class="hl">AWE</span><span class="hb">SOME</span> VETERANS!</h1>
  <p class="hero-sub">Brivolt Careers is a free job placement and coaching service<br>for military veterans.</p>
  <div class="hero-people" role="img" aria-label="Three veterans standing side by side"></div>
  <svg class="hero-arrow" style="left:40px" width="34" height="60" viewBox="0 0 34 60"><path d="M30 2 4 30l26 28" stroke="#fff" stroke-width="2" fill="none" opacity=".7"/></svg>
  <svg class="hero-arrow" style="left:1126px" width="34" height="60" viewBox="0 0 34 60"><path d="M4 2l26 28L4 58" stroke="#fff" stroke-width="2" fill="none" opacity=".7"/></svg>
  <span class="hero-dot"></span>
</section>

<h2 class="abs section-title intro-title"><span class="r">Veterans</span> &amp; Employers</h2>
<p class="abs intro-sub">Need a great jobs &amp; employee?</p>
<a class="btn btn-red" style="left:97px;top:908px;width:135px;height:45px">Register Free</a>
<div class="abs intro-divider"></div>
<p class="abs intro-text">Aenean justo dui, consequat eu consequat vel, adipiscing gravida lectus. Nunc malesuada augue non orci pellentesque hendrerit. Pellentesque neque tortor, venenatis non varius non.</p>
<a class="btn btn-blue" style="left:605px;top:908px;width:135px;height:45px">Read More</a>
<div class="abs intro-rule"></div>

<div class="card" style="left:97px">
  <svg width="80" height="84" viewBox="0 0 80 84"><path d="M40 2 76 12v28c0 22-16 36-36 42C20 76 4 62 4 40V12z" fill="#2b4c96"/><path d="M40 2v80C20 76 4 62 4 40V12z" fill="#d8343c"/><circle cx="40" cy="34" r="8" fill="#fff"/><path d="M26 56c0-9 6-14 14-14s14 5 14 14z" fill="#fff"/></svg>
  <h3>Hire A Veteran</h3>
  <p>Aenean justo dui, consequat eu consequat vel, adipiscing gravida lectus. Nunc totam rem aperiam, eaque</p>
</div>
<div class="card" style="left:451px">
  <svg width="80" height="84" viewBox="0 0 80 84"><path d="M40 2 76 12v28c0 22-16 36-36 42C20 76 4 62 4 40V12z" fill="#2b4c96"/><path d="M40 2v80C20 76 4 62 4 40V12z" fill="#d8343c"/><rect x="28" y="24" width="24" height="32" fill="#fff"/><path d="M32 34h16M32 40h16M32 46h12" stroke="#d8343c" stroke-width="2"/></svg>
  <h3>Dolore Magna Aliqua</h3>
  <p>Aenean justo dui, consequat eu consequat vel, adipiscing gravida lectus. Nunc totam rem aperiam, eaque</p>
</div>
<div class="card" style="left:804px">
  <svg width="80" height="84" viewBox="0 0 80 84"><path d="M40 2 76 12v28c0 22-16 36-36 42C20 76 4 62 4 40V12z" fill="#2b4c96"/><path d="M40 2v80C20 76 4 62 4 40V12z" fill="#d8343c"/><circle cx="40" cy="24" r="4" fill="none" stroke="#fff" stroke-width="2.5"/><path d="M40 28v30M32 36h16M26 48c2 8 8 11 14 11s12-3 14-11" stroke="#fff" stroke-width="2.5" fill="none"/></svg>
  <h3>Rem Aperiam, Eaque</h3>
  <p>Aenean justo dui, consequat eu consequat vel, adipiscing gravida lectus. Nunc totam rem aperiam, eaque</p>
</div>

<section class="videos">
  <h2 class="abs section-title videos-title"><span class="r">Our</span> <span class="r">-</span> Videos</h2>
  <p class="abs videos-lead">Aenean justo dui, consequat eu consequat vel, adipiscing gravida lectus. Nunc malesuada augue non orci pellentesque hendrerit. Pellentesque neque tortor, venenatis non varius non. rem aperiam, eaque ipsa quae ab illo ...</p>
  <div class="player">
    <div class="player-photo" role="img" aria-label="Video still of three business people joining hands in an office"></div>
    <div class="player-bar-top">Jobs is a free job placement</div>
    <div class="play-btn" style="left:227px;top:117px"><svg width="26" height="28" viewBox="0 0 26 28"><path d="M2 1l23 13L2 27z" fill="#fff"/></svg></div>
    <div class="progress"></div>
    <div class="player-bar"><span>&#9654;</span><span>&#9632;</span><span>00.00 / 2:25</span><span class="brandname">ClipTube</span></div>
  </div>
  <h4 class="abs overview-h">Over View :</h4>
  <p class="abs overview-p">Aenean justo dui, consequat eu consequat vel, adipiscing gravida lectus. Nunc totam rem aperiam, eaque... <span class="more">Read More</span></p>

  <div class="thumb" style="top:167px" role="img" aria-label="Video still of a job interview"><div class="play-btn"><svg width="12" height="14" viewBox="0 0 12 14"><path d="M1 1l10 6-10 6z" fill="#333"/></svg></div></div>
  <p class="thumb-text" style="top:165px">Aenean justo dui, consequat eu consequat vel, adipiscing gravida totam rem aperiam, eaque... <span class="more">Read More</span></p>
  <div class="thumb" style="top:317px" role="img" aria-label="Video still of a soldier greeting a family"><div class="play-btn"><svg width="12" height="14" viewBox="0 0 12 14"><path d="M1 1l10 6-10 6z" fill="#333"/></svg></div></div>
  <p class="thumb-text" style="top:315px">Aenean justo dui, consequat eu consequat vel, adipiscing gravida totam rem aperiam, eaque... <span class="more">Read More</span></p>
  <div class="thumb" style="top:465px" role="img" aria-label="Video still of a team meeting"><div class="play-btn"><svg width="12" height="14" viewBox="0 0 12 14"><path d="M1 1l10 6-10 6z" fill="#333"/></svg></div></div>
  <p class="thumb-text" style="top:463px">Aenean justo dui, consequat eu consequat vel, adipiscing gravida totam rem aperiam, eaque... <span class="more">Read More</span></p>
</section>

<h2 class="abs section-title social-title"><span class="r">Social</span> Media <span>Feeds</span></h2>
<div class="panel panel-fb">
  <div class="panel-head">Facenote</div>
  <div class="feed" style="top:40px"><div class="avatar" style="background:#c8d2e4" role="img" aria-label="Page avatar"></div><p>Laudantium, totam rem aperiam, eaque ipsa quae ab illo inve ntore veritatis et quasi architecto beatae vitae dicta...</p><small>3 minutes ago &nbsp;/&nbsp; 0 comments</small></div>
  <div class="feed" style="top:135px"><div class="avatar" style="background:#c9a98a" role="img" aria-label="Member profile photo"></div><p>Laudantium, totam rem aperiam, eaque ipsa quae ab illo inve ntore veritatis et quasi architecto beatae vitae dicta...</p><small>3 minutes ago &nbsp;/&nbsp; 0 comments</small></div>
  <div class="feed" style="top:230px;border:0"><div class="avatar" style="background:#b99880" role="img" aria-label="Member profile photo"></div><p>Laudantium, totam rem aperiam, eaque ipsa quae ab illo inve ntore veritatis et quasi architecto beatae vitae dicta...</p><small>3 minutes ago &nbsp;/&nbsp; 0 comments</small></div>
</div>
<div class="panel panel-tw">
  <div class="panel-head">Latest Twist<span style="margin-left:auto;width:16px;height:16px;border-radius:50%;background:#fff;display:inline-block"></span></div>
  <div class="feed" style="top:40px"><span class="bird"></span><p>Laudantium, totam rem aperiam, eaque ipsa quae ab illo inve ntore veritatis et quasi architecto beatae vitae dicta...</p><small>3 minutes ago &nbsp;/&nbsp; 0 comments</small></div>
  <div class="feed" style="top:135px"><span class="bird"></span><p>Laudantium, totam rem aperiam, eaque ipsa quae ab illo inve ntore veritatis et quasi architecto beatae vitae dicta...</p><small>3 minutes ago &nbsp;/&nbsp; 0 comments</small></div>
  <div class="feed" style="top:230px;border:0"><span class="bird"></span><p>Laudantium, totam rem aperiam, eaque ipsa quae ab illo inve ntore veritatis et quasi architecto beatae vitae dicta...</p><small>3 minutes ago &nbsp;/&nbsp; 0 comments</small></div>
</div>

<section class="testimonials" role="img" aria-label="Soft blurred office background">
  <h2 class="abs section-title testi-title"><span class="r">Testi</span>monials</h2>
  <div class="testi-video">
    <div class="testi-photo" role="img" aria-label="Video still of a veteran in a cap"></div>
    <div class="progress" style="bottom:36px"></div>
    <div class="player-bar"><span>&#9654;</span><span>&#9632;</span><span>00.00 / 2:25</span><span class="brandname" style="font-size:12px">ClipTube</span></div>
  </div>
  <span class="qmark" style="left:568px;top:100px">&ldquo;</span>
  <p class="quote">Aenean justo dui, consequat eu consequat vel, adipiscing gravida lectus. Nunc malesuada augue non orci pellentesque hendrerit. Pellentesque neque dislike men who are so beguiled and demoralized by the charms of pleasure of the moment, so blinded by desire, that they cannot foresee the pain and trouble that are bound to ensue; and equal blame belongs to those who fail in their duty through weakness...</p>
  <span class="qmark" style="left:712px;top:254px">&rdquo;</span>
  <p class="testi-name">-Sam Whitley <span>Groton NY</span></p>
</section>
<div class="circle-arrow" style="left:40px"><svg width="12" height="14" viewBox="0 0 12 14"><path d="M10 1 2 7l8 6" stroke="#fff" stroke-width="2.5" fill="none"/></svg></div>
<div class="circle-arrow" style="left:1126px"><svg width="12" height="14" viewBox="0 0 12 14"><path d="M2 1l8 6-8 6" stroke="#fff" stroke-width="2.5" fill="none"/></svg></div>

<footer>
  <h4 class="footer-h" style="left:97px">Informations</h4>
  <ul class="links" style="left:97px"><li>Home</li><li>Register Free</li><li>Testimonials</li><li>Hire A Veteran</li><li>About Us</li></ul>
  <ul class="links" style="left:256px"><li>Refer a Buddy</li><li>Supporters</li><li>FAQ</li><li>Job Tips</li></ul>
  <h4 class="footer-h" style="left:460px">Stay in the loop!</h4>
  <p class="loop-text">Join our confidential network and be the first know about job listings for Connecticut military veterans. We value your privacy!</p>
  <div class="field" style="top:3041px">Name</div>
  <div class="field" style="top:3075px;top:3077px">E-mail</div>
  <a class="btn btn-red subscribe">Subscribe</a>
  <h4 class="footer-h" style="left:990px">Follow Us</h4>
  <div class="follow" style="top:2970px"><i style="background:#3b5998"></i>Facenote</div>
  <div class="follow" style="top:3022px"><i style="background:#2aa3e0"></i>Chirper</div>
  <div class="follow" style="top:3074px"><i style="background:#d8443a"></i>Circle Plus</div>
  <div class="follow" style="top:3126px"><i style="background:#1b75b0"></i>WorkLink</div>
  <div class="bottom-bar">Copyrights© 2015 Brivolt Careers, &nbsp;All rights reserved.<span class="up"></span></div>
</footer>

</body>
</html>
```